Greyfield Ridge Medical Website to make connecting and communicating easier

To create a unique, user-friendly, professional website for patients and professionals to access education/ information, forms, appointments, contact details, and data about us, and for us to have the capacity to link to various cloud-based platforms.
To use the logo design and colour scheme we have just sourced.

WEBSITE to be eye catching, Inspiring and alluring
- efficient and logical
- professional and trustworthy appearance
- health focus "living health matters"
- user friendly
- ability to link with cloud-based software and video conferencing tools/ telehealth
- colours- black/ white teal and ?silver

PAGES:
page 1 - Our clinic and staff, services offered, contact us- address/ map / contact details- social media connections
page 2- patients and visitors - New patient forms to complete, news and patient informtion (educatinal)
page 3 - health professionals -referral forms, research and education
page 3- online appointments
page 4 - Quick links - partners, other services
page 5- privacy policy, disclaimer

HI, Could we please extend the deadline another 5 days, so sorry just struggling with my workload to be able to keep up and I am wanting to liaise more with the designer that I will choose. I am so happy with PixelHarbor and all the designers - thank you! Thank you so much!!

Target Market(s)

Patients - mostly over 60's so the website must be minimal clicks and simple to navigate
Professionals - for education and access forms

Industry/Entity Type

Health Care

Coding

Coded - Design and coding required

Number of Pages Required

5+ page

Font styles to use
Sans Serif
Script

Colors
33b8a4
86cfc6

Requirements
Must have
• WEBSITE to be eye catching, Inspiring and alluring
- efficient and logical
- user friendly

WEBSITE - professional and user friendly
- ability to link with cloud based software and videoconferencing/ telehealth
Nice to have
• clean and crisp presentation
happy for an innovative look
room to add more services and ability to link pages and resources
Should not have
• Please ensure the website is not:
clunky
difficult to navigate
common and cheap looking

```html
<!DOCTYPE html>
<html lang="en">
<head>
<meta charset="utf-8">
<title>Greyfield Ridge Medical – Online Appointment</title>
<link href="https://fonts.googleapis.com/css2?family=Montserrat:wght@400;500;600;700&family=Questrial&display=swap" rel="stylesheet">
<style>
:root{
  --teal:#33b8a4;
  --teal-light:#86cfc6;
  --teal-pale:#b9e6e0;
  --teal-deep:#058a7b;
  --slot-off:#c4c4c4;
  --ink:#111;
  --line:#b8b8b8;
  --white:#fff;
  --black:#000;
}
*{box-sizing:border-box;margin:0;padding:0}
html,body{width:856px;height:1200px;overflow:hidden}
body{position:relative;background:var(--white);font-family:"Montserrat",sans-serif;color:var(--ink)}

/* header */
.site-header{position:absolute;left:0;top:0;width:856px;height:64px;background:var(--white)}
.brand{position:absolute;left:131px;top:22px;font-size:12px;font-weight:600;color:var(--teal);line-height:1.1;width:110px}
.main-nav{position:absolute;top:27px;left:356px;font-family:"Questrial",sans-serif;font-size:11.5px;color:#333}
.main-nav a{color:inherit;text-decoration:none;position:absolute;white-space:nowrap}
.header-social{position:absolute;top:23px;left:614px;display:flex;gap:5px}
.header-social span{width:24px;height:24px;border-radius:50%;background:var(--teal-pale)}

/* hero */
.hero{position:absolute;left:0;top:64px;width:856px;height:268px;background:var(--teal-deep)}
.hero-art-left{position:absolute;left:21px;top:112px;width:238px;height:156px;border-radius:6px;background:linear-gradient(135deg,#f17468 0%,#f4f4f4 35%,#5b72d0 100%)}
.hero-art-right{position:absolute;left:649px;top:48px;width:171px;height:220px;border-radius:14px;background:linear-gradient(180deg,#e8ecea 0%,#f0f0f0 55%,#1ab2a0 100%)}
.hero-title{position:absolute;left:247px;top:110px;width:362px;font-family:"Questrial",sans-serif;font-weight:400;font-size:36px;color:var(--white);letter-spacing:1.6px;white-space:nowrap}

/* booking */
.section-title{position:absolute;left:0;width:856px;top:374px;text-align:center;font-family:"Questrial",sans-serif;font-weight:400;font-size:30px;letter-spacing:1.6px;color:var(--ink)}
.title-rule{position:absolute;left:415px;top:424px;width:26px;height:2px;background:var(--teal)}
.field{position:absolute;height:33px;border:1px solid var(--line);border-radius:17px;display:flex;align-items:center;padding-left:16px;font-size:9px;color:#333}
.field svg{width:10px;height:10px;margin-right:6px;fill:#555}
.field .caret{position:absolute;right:20px;top:13px;width:0;height:0;border-left:4px solid transparent;border-right:4px solid transparent;border-top:5px solid #444}

.schedule{position:absolute;left:166px;top:599px;width:524px;height:223px;border:1px solid var(--line);border-radius:4px;overflow:hidden}
.days{display:flex;height:38px;background:#f3f3f3;border-bottom:1px solid var(--line)}
.day{width:75px;border-right:1px solid var(--line);text-align:center;padding-top:8px;position:relative}
.day:last-child{border-right:none}
.day b{display:block;font-size:8.5px;font-weight:600;color:#111}
.day small{display:block;font-size:5.5px;color:#777;margin-top:2px}
.day.active{background:var(--white);border:1px solid #555;height:39px}
.day.active::after{content:"";position:absolute;left:32px;bottom:-6px;width:8px;height:8px;background:var(--white);border-right:1px solid #555;border-bottom:1px solid #555;transform:rotate(45deg)}
.slots{position:absolute;left:4px;top:53px;display:grid;grid-template-columns:repeat(7,70px);grid-auto-rows:38.5px;gap:4px}
.slot{background:var(--teal-light);color:var(--white);font-size:9.5px;font-weight:600;display:flex;align-items:center;justify-content:center}
.slot.off{background:var(--slot-off);color:#666}
.slot.on{background:var(--teal);border:2px solid var(--teal-light)}

.book-btn{position:absolute;left:365px;top:850px;width:126px;height:33px;border-radius:17px;background:var(--teal);color:var(--white);font-size:11px;font-weight:600;display:flex;align-items:center;justify-content:center}

/* footer */
.site-footer{position:absolute;left:0;top:937px;width:856px;height:263px;background:var(--black);color:var(--white)}
.footer-brand{position:absolute;left:136px;top:82px;font-size:15px;font-weight:600;color:var(--teal);line-height:1.15;width:100px}
.lang{position:absolute;left:131px;top:144px;width:100px;height:24px;border:1px solid var(--white);display:flex;align-items:center;padding-left:19px;font-size:7.5px;font-weight:600}
.lang i{width:9px;height:9px;border-radius:50%;background:#c9d4ea;margin-right:4px}
.lang em{position:absolute;right:15px;top:10px;border-left:2.5px solid transparent;border-right:2.5px solid transparent;border-top:3px solid var(--white)}
.col-head{position:absolute;font-size:11px;font-weight:700}
.col-head::after{content:"";position:absolute;left:0;top:21px;width:14px;height:2px;background:var(--teal)}
.quick-links{position:absolute;left:279px;top:82px;list-style:none;font-size:7.5px;line-height:16px}
.contact-item{position:absolute;left:399px;display:flex;font-size:6.5px;line-height:10px}
.contact-item svg{width:9px;height:9px;fill:var(--white);margin:0 9px 0 3px}
.contact-item b{font-weight:700}
.footer-social{position:absolute;left:551px;top:86px;display:flex;gap:5px}
.footer-social span{width:25px;height:25px;border-radius:50%;background:var(--teal)}
.footer-rule{position:absolute;left:131px;top:223px;width:594px;height:1px;background:#333}
.legal{position:absolute;top:238px;font-size:8px}
</style>
</head>
<body>

<header class="site-header">
  <div class="brand">Greyfield Ridge Medical</div>
  <nav class="main-nav">
    <a style="left:0">Home</a>
    <a style="left:61px">Staff</a>
    <a style="left:113px">Services</a>
    <a style="left:185px">Contact Us</a>
  </nav>
  <div class="header-social" aria-label="Social links"><span></span><span></span><span></span><span></span></div>
</header>

<section class="hero">
  <div class="hero-art-left" role="img" aria-label="Illustration of a man marking a large desk calendar"></div>
  <h1 class="hero-title">Online Appointment</h1>
  <div class="hero-art-right" role="img" aria-label="Illustration of a woman on the phone beside a wall calendar"></div>
</section>

<h2 class="section-title">Book Online Appointment</h2>
<div class="title-rule"></div>

<div class="field" style="left:166px;top:453px;width:254px"><svg viewBox="0 0 10 10"><circle cx="5" cy="3" r="2.4"/><path d="M0.5 10c0-3 2-4.5 4.5-4.5S9.5 7 9.5 10z"/></svg>First Name*</div>
<div class="field" style="left:436px;top:453px;width:254px"><svg viewBox="0 0 10 10"><circle cx="5" cy="3" r="2.4"/><path d="M0.5 10c0-3 2-4.5 4.5-4.5S9.5 7 9.5 10z"/></svg>Last Name*</div>
<div class="field" style="left:166px;top:501px;width:254px"><svg viewBox="0 0 10 10"><path d="M2.5 0h5v10h-5zM3.3 1v7h3.4V1z"/></svg>Phone Number*</div>
<div class="field" style="left:436px;top:501px;width:254px"><svg viewBox="0 0 10 10"><path d="M0 2h10v6H0zM0.8 2.6 5 5.8 9.2 2.6z" fill-rule="evenodd"/></svg>Email Address*</div>
<div class="field" style="left:166px;top:550px;width:524px"><svg viewBox="0 0 10 10"><circle cx="3" cy="4" r="1.6"/><circle cx="7" cy="3.4" r="1.6"/><path d="M0 10c0-2.5 1.4-4 3-4s3 1.5 3 4zM4.5 10c0-3 1-4.7 2.5-4.7S10 7 10 10z"/></svg>Reson For Visit<span class="caret"></span></div>

<div class="schedule">
  <div class="days">
    <div class="day"><b>Monday</b><small>07:00 AM, 07:PM</small></div>
    <div class="day"><b>Tuesday</b><small>07:00 AM, 07:PM</small></div>
    <div class="day"><b>Wednesday</b><small>07:00 AM, 07:PM</small></div>
    <div class="day active"><b>Thursday</b><small>07:00 AM, 07:PM</small></div>
    <div class="day"><b>Friday</b><small>07:00 AM, 07:PM</small></div>
    <div class="day"><b>Saturday</b><small>07:00 AM, 07:PM</small></div>
    <div class="day"><b>Sunday</b><small>07:00 AM, 07:PM</small></div>
  </div>
  <div class="slots">
    <div class="slot">07:00 AM</div><div class="slot off">07:30 AM</div><div class="slot">08:00 AM</div><div class="slot">08:30 AM</div><div class="slot">09:00 AM</div><div class="slot">09:30 AM</div><div class="slot">10:00 AM</div>
    <div class="slot off">10:30 AM</div><div class="slot">11:00 AM</div><div class="slot">11:30 AM</div><div class="slot">12:00 PM</div><div class="slot">12:30 PM</div><div class="slot off">01:00 PM</div><div class="slot">01:30 PM</div>
    <div class="slot">02:00 PM</div><div class="slot off">02:30 PM</div><div class="slot">03:00 PM</div><div class="slot on">03:30 PM</div><div class="slot">04:00 PM</div><div class="slot">04:30 PM</div><div class="slot off">05:00 PM</div>
    <div class="slot off">05:30 PM</div><div class="slot">06:00 PM</div><div class="slot">06:30 PM</div><div class="slot">07:00 PM</div>
  </div>
</div>

<div class="book-btn">Book Now!</div>

<footer class="site-footer">
  <div class="footer-brand">Greyfield Ridge Medical</div>
  <div class="lang"><i></i>English<em></em></div>

  <div class="col-head" style="left:279px;top:58px">Quick Links</div>
  <ul class="quick-links">
    <li>Home</li><li>Staff</li><li>Services</li><li>Contact Us</li><li>Patients</li><li>Health Professionals</li>
  </ul>

  <div class="col-head" style="left:399px;top:58px">Contact Us</div>
  <div class="contact-item" style="top:90px"><svg viewBox="0 0 10 10"><path d="M5 0a3.5 3.5 0 0 1 3.5 3.5C8.5 6 5 10 5 10S1.5 6 1.5 3.5A3.5 3.5 0 0 1 5 0zm0 2a1.4 1.4 0 1 0 0 2.8A1.4 1.4 0 0 0 5 2z"/></svg><span>Greyfield Ridge Medical</span></div>
  <div class="contact-item" style="top:110px"><svg viewBox="0 0 10 10"><path d="M2.5 0h5v10h-5zM3.3 1v7h3.4V1z"/></svg><span><b>Call Us:</b><br>02 4917 3360</span></div>
  <div class="contact-item" style="top:139px"><svg viewBox="0 0 10 10"><path d="M0 2h10v6H0zM0.8 2.6 5 5.8 9.2 2.6z" fill-rule="evenodd"/></svg><span><b>Email.Us:</b><br>hello@greyfieldridge.com</span></div>

  <div class="col-head" style="left:551px;top:61px">Get Social</div>
  <div class="footer-social" aria-label="Social links"><span></span><span></span><span></span><span></span></div>

  <div class="footer-rule"></div>
  <div class="legal" style="left:131px">Copyright © Greyfield Ridge Medical 2020. All right Reserved</div>
  <div class="legal" style="right:131px">Privacy Policy, Disclaimer</div>
</footer>

</body>
</html>
```